Flyer design for retail store owners

i would need to have a flyer design for my retail shop customers to show that I am a mailbox store that has all major shipping vendors to for their shipping needs. Ensuring that they can take advantage of opening a house account at the store and billed monthly, word document has all the details. Please use stock images for the notary public, passport photos, mailbox brass pictures of my actual mailboxes are listed in the pictures. I need to make it POP and WOW these retail store owners as I am using it to advertise the business

```html
<!DOCTYPE html>
<html lang="en">
<head>
<meta charset="utf-8">
<title>Mailbox Rental Flyers</title>
<link href="https://fonts.googleapis.com/css2?family=Arimo:wght@400;700&display=swap" rel="stylesheet">
<style>
:root{
  --red:#e8202a;
  --yellow:#fcc614;
  --white:#ffffff;
  --paper:#f1f1f1;
  --backdrop:#ececec;
  --ink:#333333;
  --muted:#6a6a6a;
  --brass-light:#d3a874;
  --brass-dark:#8a6a3c;
  --bronze-light:#9c8e66;
  --bronze-dark:#5e5234;
}
*{margin:0;padding:0;box-sizing:border-box}
html,body{width:779px;height:1200px;overflow:hidden;background:var(--backdrop)}
body{font-family:"Arimo",Arial,sans-serif;position:relative}

.flyer{position:absolute;top:342px;width:635px;height:890px;overflow:hidden;
  transform:scale(.58);transform-origin:0 0;box-shadow:0 6px 18px rgba(0,0,0,.18)}
.flyer > *{position:absolute}
.flyer-offer{left:14px;background:radial-gradient(circle at 85% 15%,var(--paper),var(--white) 55%)}
.flyer-partners{left:397px;background:var(--white)}

.headline{top:22px;left:0;width:100%;text-align:center;color:var(--red);
  font-weight:700;font-size:37px;line-height:44px;letter-spacing:.3px;white-space:nowrap}
.location-band{top:64px;left:40px;width:555px;height:25px;color:var(--white);
  font-weight:700;font-size:21px;line-height:25px;text-align:center;letter-spacing:.3px;white-space:nowrap}
.flyer-offer .location-band{background:var(--yellow)}
.flyer-partners .location-band{background:var(--red)}

/* offer flyer */
.intro{top:108px;left:75px;width:485px;height:83px;border:1px solid var(--red);
  padding:5px 6px;color:var(--ink);font-size:9.3px;line-height:12px;text-align:center}
.photo{top:204px;height:205px}
.photo-cabinet{left:24px;width:181px;background:linear-gradient(135deg,var(--brass-light),var(--brass-dark))}
.photo-doors{left:225px;width:172px;background:linear-gradient(135deg,#d8ae7a,#a47c48)}
.photo-brass{left:414px;width:203px;top:222px;height:173px;background:linear-gradient(135deg,var(--bronze-light),var(--bronze-dark))}
.offer-band{top:404px;left:0;width:100%;height:175px;background:var(--red)}
.offer-text{top:420px;left:0;width:100%;color:var(--white);font-size:13.3px;line-height:24px;
  text-align:center;white-space:nowrap}
.offer-text .hl{color:var(--yellow);font-weight:700;font-size:18px}
.offer-text b{font-weight:700}
.benefits-band{top:579px;left:0;width:100%;height:311px;background:var(--yellow)}
.cta-banner{top:562px;left:30px;width:575px;height:37px;background:var(--yellow);
  border:1.5px solid var(--red);border-radius:12px;color:var(--red);font-weight:700;
  font-size:18.5px;line-height:34px;text-align:center;white-space:nowrap}
.benefits{top:622px;left:26px;width:590px;list-style:none}
.benefits li{position:relative;padding-left:24px;color:#222;font-weight:700;font-size:12.3px;
  line-height:21px;margin-bottom:18px;white-space:nowrap}
.benefits li::before{content:"➢";position:absolute;left:0;top:0;font-size:9px}
.benefits .hl{color:var(--red);font-size:17px}

/* partners flyer */
.top-band{top:0;left:0;width:100%;height:384px;background:var(--yellow)}
.about{top:107px;left:38px;width:557px;height:106px;border:1px solid var(--red);
  padding:4px 7px;color:var(--red);font-size:12.4px;line-height:19.4px;
  text-align:justify;text-align-last:center}
.photo-wall{top:244px;left:26px;width:582px;height:290px;
  background:linear-gradient(160deg,#8f8d6c,#6e6a4c 55%,#8a7e5c)}
.partners-banner{top:556px;left:26px;width:584px;height:58px;background:var(--red);
  border-radius:10px 16px 16px 10px;color:var(--white);font-size:31px;line-height:58px;
  text-align:center;white-space:nowrap}
.partner-slot{top:641px;height:85px;border:1px solid var(--red);background:var(--white);
  display:flex;align-items:center;justify-content:center}
.partner-slot span{display:block;width:44px;height:44px;background:#d9d9d9}
.slot-1{left:30px;width:170px}
.slot-2{left:215px;width:118px}
.slot-3{left:346px;width:119px}
.slot-4{left:485px;width:120px}
.slot-4 span{width:96px;height:66px;background:var(--yellow)}
.summary{top:751px;left:28px;width:580px;height:86px;border:1px solid var(--red);
  border-radius:14px;padding:6px 8px;color:var(--muted);font-size:11px;line-height:19.5px;
  text-align:center}
.summary .red{color:var(--red);font-weight:700}
.summary .gold{color:#e8a800}
</style>
</head>
<body>

<main class="flyer flyer-offer">
  <h1 class="headline">NOW RENTING MAILBOXES ON</h1>
  <div class="location-band">MAPLE RIDGE CROSSING SHOPPING CENTER</div>
  <p class="intro">Renting a mail box is one of the most efficient and cost saving methods for receiving your mail and packages. Instead of having to worry about private security, weather conditions, sorting, and deliveries; all you have to do is pick-up your mail from our secured facility each day except Sundays. You will get a notification when mail arrives whether envelope or package, it will be scanned in daily which other mailbox stores do not offer! We offer onsite Notary Public with no appointments and onsite Passport Photos and can ship out same day.</p>

  <div class="offer-band"></div>
  <div class="benefits-band"></div>

  <div class="photo photo-cabinet" role="img" aria-label="Photo of a tan mailbox cabinet shown at an angle with rows of small locking doors"></div>
  <div class="photo photo-doors" role="img" aria-label="Photo of a tan mailbox panel with a grid of numbered locking doors"></div>
  <div class="photo photo-brass" role="img" aria-label="Photo of the store's vintage brass mailbox wall"></div>

  <p class="offer-text">Now renting mailboxes on Maple Ridge Crossing Shopping Center. We are offering all<br>Maple Ridge crossing shopping center owners/employees an exclusive promo deal! <span class="hl">$12</span><br>a month for <span class="hl">6-12 months</span> leases! You get a mailbox in the shop, a book of<br>stamps(20 count), 3 notarizations by appointment, <b>100 copies</b> of black and white, and<br><b>100 copies</b> of color. Please see associate for sign up!</p>

  <div class="cta-banner">TAKE ADVANTAGE OF THIS LIMITED TIME OFFER NOW!</div>

  <ul class="benefits">
    <li>As a retail owner, you know how important it is to keep your customers<br>coming back - you will get <span class="hl">20%</span> discount for printing services.</li>
    <li>We duplicate keys for <span class="hl">$2</span>/each, our regular price charge is <span class="hl">$4</span>/each. Save up to <span class="hl">50%</span>!</li>
    <li>Lamination is also discounted at <span class="hl">10%</span> off.</li>
    <li><span class="hl">10%</span> off retail supplies ... must be minimum of <span class="hl">10$</span></li>
    <li>For house accounts -a <span class="hl">5%</span> discount will be deducted monthly of billing change to<br>invoicing PLUS we're giving another <span class="hl">5%</span> of the discount if you upgrade and sign<br>up for mailbox. Great right?</li>
  </ul>
</main>

<main class="flyer flyer-partners">
  <div class="top-band"></div>
  <h1 class="headline">NOW RENTING MAILBOXES ON</h1>
  <div class="location-band">MAPLE RIDGE CROSSING SHOPPING CENTER</div>
  <p class="about">At Swift Parcel &amp; Post, our goal is to make your shipping experience as convenient as possible. Whether you are shipping packages, documents, or packages, we are here to help. Whether you want to track your package or estimate the price of your package, it is easy for you. We are ready to handle all of your postal services! Get also the services you need; printing, copying, and stop in to purchase postage or shipping materials</p>

  <div class="photo-wall" role="img" aria-label="Photo of the store's aged brass mailbox wall with a row of small doors"></div>

  <div class="partners-banner">SERVICE POINT PARTNERS ARE</div>

  <div class="partner-slot slot-1" role="img" aria-label="Shipping partner badge"><span></span></div>
  <div class="partner-slot slot-2" role="img" aria-label="Shipping partner badge"><span></span></div>
  <div class="partner-slot slot-3" role="img" aria-label="Shipping partner badge"><span></span></div>
  <div class="partner-slot slot-4" role="img" aria-label="Shipping partner badge"><span></span></div>

  <p class="summary">Now renting mailboxes on Maple Ridge Crossing Shopping Center. We are offering all Maple Ridge crossing shopping center owners/employees an exclusive promo deal! <span class="red">$12</span> a month for <span class="gold">6-12 months</span> leases! You get a mailbox in the shop, a book of stamps(20 count), 3 notarizations by appointment, 100 copies of black and white, and 100 copies of color. Please see associate for sign up!</p>
</main>

</body>
</html>
```